Recruitment Firm Business Card

I need to design my business cards for my new recruitment company, Brightpath Staffing.

I already have the logo and colours, so half work is already done.

I would like the back of the cards just to be the black background version of the logo...so all black with the logo in the middle.

For the front of the cards I would like it to be white with the small white background version of the logo and the following information:

Maris Kotter
Brightpath Staffing
Managing Director | Application Development Specialist
-----------------------------------------------------------------------

p | +61 2 8156 3042 e | maris@brightpathstaffing.com.au
m | +61 (0)438714926 w | www.brightpathstaffing.com.au

Tarrow Bank Tower
Level 14/ 8 Penhale Street
Sydney, NSW 2000

In terms of how this information is presented I am flexible and open to ideas.

Just please stick to the colour theme - light blue, black and white and make as professional as possible.

```html
<!DOCTYPE html>
<html lang="en">
<head>
<meta charset="utf-8">
<title>Brightpath Staffing – Business Card</title>
<link rel="stylesheet" href="https://fonts.googleapis.com/css2?family=Cinzel:wght@500&family=Open+Sans:wght@400;600&family=Tinos&display=swap">
<style>
  :root {
    --page: #e6e7e9;
    --card-white: #ffffff;
    --card-black: #161616;
    --blue: #1f8fcf;
    --blue-light: #7fd0ea;
    --blue-pale: #d6f0f8;
    --ink: #1a1a1a;
    --grey: #5a5a5a;
    --rule: #9a9a9a;
  }
  * { box-sizing: border-box; margin: 0; padding: 0; }
  html, body { width: 1200px; height: 900px; overflow: hidden; }
  body {
    background: var(--page);
    position: relative;
  }
  .card {
    position: absolute;
    left: 300px;
    width: 600px;
    height: 366px;
    border-radius: 4px;
    overflow: hidden;
    box-shadow: 0 6px 18px rgba(0,0,0,0.18);
  }
  .card--front { top: 48px; background: var(--card-white); }
  .card--back { top: 486px; background: var(--card-black); }

  .holder-name {
    position: absolute;
    left: 30px; top: 30px;
    font-family: "Cinzel", serif;
    font-weight: 500;
    font-size: 29px;
    letter-spacing: 1px;
    color: var(--blue);
    white-space: nowrap;
  }
  .brand {
    position: absolute;
    display: flex;
    align-items: center;
    gap: 10px;
    font-family: "Open Sans", sans-serif;
    font-weight: 400;
    white-space: nowrap;
  }
  .brand__dot {
    border-radius: 50%;
    border: 3px solid var(--blue);
    flex: none;
  }
  .brand--small { right: 26px; top: 28px; }
  .brand--small .brand__dot { width: 34px; height: 34px; }
  .brand--small .brand__name { font-size: 20px; color: var(--grey); }

  .company {
    position: absolute;
    left: 30px; top: 78px;
    font-family: "Open Sans", sans-serif;
    font-size: 17px;
    color: var(--ink);
  }
  .role {
    position: absolute;
    left: 30px; top: 100px;
    font-family: "Open Sans", sans-serif;
    font-size: 13.5px;
    color: var(--ink);
    white-space: nowrap;
  }
  .divider {
    position: absolute;
    left: 30px; top: 132px;
    width: 400px;
    border-top: 2px dotted var(--rule);
  }
  .contact {
    position: absolute;
    left: 30px; top: 146px;
    font-family: "Tinos", serif;
    font-size: 13.5px;
    line-height: 22px;
    color: var(--ink);
    white-space: nowrap;
  }
  .address {
    position: absolute;
    left: 30px; top: 206px;
    font-family: "Open Sans", sans-serif;
    font-weight: 600;
    font-size: 12.5px;
    line-height: 21px;
    color: var(--ink);
  }
  .wave-band {
    position: absolute;
    left: 0; bottom: 0;
    width: 600px; height: 80px;
    background: linear-gradient(180deg, var(--blue-pale) 0%, var(--blue-light) 55%, var(--blue) 100%);
  }

  .brand--large {
    left: 50%; top: 50%;
    transform: translate(-50%, -50%);
    gap: 18px;
  }
  .brand--large .brand__dot { width: 64px; height: 64px; border-width: 5px; }
  .brand--large .brand__name { font-size: 42px; color: #ffffff; }
</style>
</head>
<body>

<section class="card card--front" aria-label="Front of business card">
  <div class="wave-band" role="img" aria-label="Decorative light blue wave band along the bottom of the card"></div>

  <h1 class="holder-name">MARIS KOTTER</h1>

  <div class="brand brand--small">
    <span class="brand__dot"></span>
    <span class="brand__name">Brightpath Staffing</span>
  </div>

  <p class="company">Brightpath Staffing</p>
  <p class="role">Managing Director | Application Development Specialist</p>
  <div class="divider"></div>

  <p class="contact">
    p | +61 2 8156 3042 e | maris@brightpathstaffing.com.au<br>
    m | +61 (0)438714926 w | www.brightpathstaffing.com.au
  </p>

  <p class="address">
    Tarrow Bank Tower<br>
    Level 14/ 8 Penhale Street<br>
    Sydney, NSW 2000
  </p>
</section>

<section class="card card--back" aria-label="Back of business card">
  <div class="brand brand--large">
    <span class="brand__dot"></span>
    <span class="brand__name">Brightpath Staffing</span>
  </div>
</section>

</body>
</html>
```